App Design - Job Poise Lantern

We require an App Design for our new App called 'Poise Lantern'. This app is essentially an assistant to help Users prepare for job interviews, to help them get hired. <br/><br/>Users who download the App can view common Questions and Answers, save their favourite responses and also view common Interview Tips. <br/><br/>The vision for our App is for Users who are preparing for an interview (1 week before, 1 day before, even 1 hour before), are able to download, view and educate themselves on common questions and responses, and then be confident to land the job. <br/><br/>Our team has developed wireframes to help highlight what each screen should do and include. Please see attached document, which also highlights key requirements for the experience. Feel free to add/remove/edit what you see on these wireframes. Our preference is that you use Adobe XD please.<br/><br/>In terms of design guidelines, we want the experience to be simple, intuitive and 'memorable' to help Users to remember the questions/responses when they are in the interview. <br/><br/>The final design should communicate 'neat and clean professionalism'; we like the design of: vocatia hub com au<br/><br/>Thank you for reading! Good luck !

Target Market(s)

Professional job seekers

Font styles to use
Sans Serif

Colors

Designer to choose colors to be used in the design.

Requirements
Must have
• Please see my PixelBazaar_UX file that I have uploaded
Nice to have
• Could you also please include some ideas on how we can incorporate Advertising into the app screens

```html
<!DOCTYPE html>
<html lang="en">
<head>
<meta charset="utf-8">
<title>Poise Lantern – App Screens</title>
<link href="https://fonts.googleapis.com/css2?family=Rubik:wght@400;500;700&display=swap" rel="stylesheet">
<style>
:root{
  --blue:#4b5efe;
  --blue-soft:#c9cffd;
  --teal:#00c4a0;
  --red:#ff4d5e;
  --yellow:#ffc600;
  --ink:#272a3d;
  --muted:#5d6072;
  --surface:#f1f2f7;
  --card:#ffffff;
  --canvas:#ffffff;
}
*{box-sizing:border-box;margin:0;padding:0}
html,body{width:1200px;height:2338px;overflow:hidden;background:var(--canvas)}
body{position:relative;font-family:'Rubik',sans-serif;color:var(--ink)}

.screen{position:absolute;width:322px;height:702px;overflow:hidden;background:var(--surface);
  border-radius:34px;transform:scale(.898);transform-origin:0 0;box-shadow:0 18px 40px rgba(75,94,254,.12)}
.screen--blue{background:var(--blue)}
.c1{left:99px}.c2{left:454px}.c3{left:811px}
.r1{top:119px}.r2{top:841px}.r3{top:1562px}

.app-bar{height:88px;background:var(--blue);position:relative;display:flex;align-items:flex-end;justify-content:center;padding-bottom:18px}
.app-bar .back{position:absolute;left:18px;bottom:20px;width:14px;height:20px}
.wordmark{color:#fff;font-weight:700;font-size:19px;letter-spacing:.2px}

.section-bar{height:57px;background:var(--card);display:flex;align-items:center;gap:14px;padding-left:20px;border-bottom:1px solid #e2e3ea}
.section-bar--center{justify-content:center;padding-left:0}
.section-bar h2{font-size:16px;font-weight:500;color:var(--ink)}

.dot-icon{width:34px;height:34px;border-radius:50%;display:flex;align-items:center;justify-content:center;color:#fff;font-weight:700;font-size:15px;flex:none}
.dot-icon svg{width:18px;height:18px}
.dot-icon--teal{background:var(--teal);box-shadow:0 4px 10px rgba(0,196,160,.35)}
.dot-icon--red{background:var(--red);box-shadow:0 4px 10px rgba(255,77,94,.35)}
.dot-icon--yellow{background:var(--yellow);box-shadow:0 4px 10px rgba(255,198,0,.35)}
.dot-icon .q{width:18px;height:18px;border-radius:50%;background:rgba(255,255,255,.3);display:flex;align-items:center;justify-content:center;font-size:11px}

.prompt{text-align:center;font-size:12px;color:var(--ink);margin:40px 0 28px}

.choice-list{display:flex;flex-direction:column;gap:29px;padding:0 20px}
.choice{height:55px;background:var(--card);border-radius:6px;display:flex;align-items:center;justify-content:center;gap:12px;
  color:var(--blue);font-weight:500;font-size:15px;box-shadow:0 6px 0 -2px var(--blue-soft),0 8px 14px rgba(75,94,254,.12)}
.choice--left{justify-content:flex-start;padding-left:14px}
.choice svg{width:18px;height:18px}

.pill-btn{display:block;margin:30px auto 0;width:166px;height:40px;border-radius:6px;background:var(--blue);color:#fff;
  font-size:14px;font-weight:500;display:flex;align-items:center;justify-content:center}

/* splash */
.splash{display:flex;flex-direction:column;align-items:center;color:#fff;text-align:center}
.splash .mark{margin-top:150px;width:70px;height:70px;border-radius:50%;background:var(--teal)}
.splash .wordmark{font-size:27px;margin-top:60px}
.splash p{font-size:13.5px;font-weight:500;line-height:19px;margin-top:24px;padding:0 28px;color:#e9ebff}
.splash .start{position:absolute;left:20px;right:20px;bottom:58px;height:55px;border-radius:4px;background:var(--surface);
  color:var(--blue);font-size:18px;font-weight:500;display:flex;align-items:center;justify-content:center;box-shadow:0 6px 14px rgba(0,0,0,.15)}

/* welcome */
.welcome-head{position:absolute;left:25px;top:60px}
.welcome-head .hello{font-size:20px;color:#8a8c99}
.welcome-head .name{font-size:24px;font-weight:700;color:var(--blue);margin-top:8px}
.welcome-wave{position:absolute;left:0;top:0;width:322px;height:702px}
.welcome-art{position:absolute;left:40px;top:150px;width:250px;height:170px;border-radius:12px;
  background:linear-gradient(160deg,rgba(255,255,255,.35),rgba(75,94,254,.25))}
.menu{position:absolute;left:16px;right:16px;top:348px;display:flex;flex-direction:column;gap:30px}
.menu-card{height:76px;border-radius:6px;background:var(--surface);display:flex;align-items:center;gap:20px;padding-left:14px;
  font-size:13.5px;font-weight:500;box-shadow:0 8px 16px rgba(20,30,120,.2)}
.menu-card .dot-icon{width:46px;height:46px}

/* numbered lists */
.band{color:#fff;font-weight:500;font-size:14px;display:flex;align-items:center;justify-content:center;gap:8px;height:36px}
.band svg{width:14px;height:14px}
.band--teal{background:var(--teal)}
.stack{display:flex;flex-direction:column;gap:20px;padding:14px 14px 0}
.item{background:var(--card);border-radius:6px;display:flex;align-items:center;gap:16px;padding:10px 14px 10px 8px;
  box-shadow:0 4px 10px rgba(30,40,90,.08)}
.item p{font-size:12px;line-height:16px;color:var(--ink)}
.num{width:24px;height:24px;border-radius:4px;color:#fff;font-size:12px;font-weight:700;display:flex;align-items:center;justify-content:center;flex:none}
.num--teal{background:var(--teal);box-shadow:0 3px 6px rgba(0,196,160,.4)}
.num--yellow{background:var(--yellow);box-shadow:0 3px 6px rgba(255,198,0,.4)}
.num--red{background:var(--red);box-shadow:0 3px 6px rgba(255,77,94,.4)}

.carousel{padding:10px 0 12px;position:relative}
.carousel--teal{background:var(--teal)}
.carousel--yellow{background:var(--yellow)}
.carousel .item{margin:0 14px}
.carousel .peek{position:absolute;top:10px;width:8px;height:80px;background:var(--card);border-radius:4px}
.carousel .peek--l{left:0;border-radius:0 4px 4px 0}
.carousel .peek--r{right:0;border-radius:4px 0 0 4px}
.dots{display:flex;gap:8px;justify-content:center;margin-top:16px}
.dots i{width:5px;height:5px;border-radius:50%;background:rgba(255,255,255,.55)}
.dots i:first-child{background:#fff}

.responses{display:flex;flex-direction:column;gap:16px;padding:8px 10px 0}
.response{background:var(--card);border-radius:6px;position:relative;padding:30px 14px 10px;box-shadow:0 4px 10px rgba(30,40,90,.08)}
.response .tag{position:absolute;left:0;top:0;background:var(--teal);color:#fff;font-size:10px;font-weight:500;padding:3px 10px;border-radius:6px 0 6px 0}
.response p{font-size:12px;line-height:16px}
.response .fav{position:absolute;right:6px;top:4px;width:18px;height:16px}

/* portfolio */
.intro{text-align:center;font-size:12px;line-height:16px;color:var(--muted);padding:14px 10px 0}
.saved{display:flex;flex-direction:column;gap:18px;padding:22px 14px 0}
.saved-card{background:var(--card);border-radius:6px;padding:12px 28px 14px 56px;position:relative;box-shadow:0 4px 10px rgba(30,40,90,.08)}
.saved-card .num{position:absolute;left:8px;top:12px}
.saved-card h3{font-size:12.5px;font-weight:500;line-height:16px;margin-bottom:10px}
.saved-card p{font-size:12px;line-height:16px;color:var(--muted)}
.saved-card .remove{position:absolute;right:10px;top:10px;width:16px;height:16px;border-radius:50%;background:#ffe1e4}

/* tip detail */
.tip-body{margin:22px 14px 0;background:var(--card);border-radius:6px;padding:14px 18px;font-size:12px;line-height:16px;color:var(--muted);box-shadow:0 4px 10px rgba(30,40,90,.08)}
.ad-slot{position:absolute;left:0;right:0;bottom:0;height:46px;background:linear-gradient(90deg,#5d7dbd,#c89a5a,#8a5d3a)}
</style>
</head>
<body>

<svg width="0" height="0" style="position:absolute">
  <defs>
    <symbol id="chev" viewBox="0 0 14 20"><path d="M11 2 3 10l8 8" fill="none" stroke="#fff" stroke-width="2.5" stroke-linecap="round" stroke-linejoin="round"/></symbol>
    <symbol id="heart" viewBox="0 0 20 18"><path d="M10 17 2.5 9.6A4.6 4.6 0 0 1 10 3.7a4.6 4.6 0 0 1 7.5 5.9Z" fill="currentColor"/></symbol>
    <symbol id="bulb" viewBox="0 0 20 20"><circle cx="10" cy="8" r="6" fill="#fff"/><rect x="7" y="13" width="6" height="5" rx="1.5" fill="#fff"/></symbol>
    <symbol id="puzzle" viewBox="0 0 16 16"><path d="M2 5h3a2 2 0 1 1 4 0h3v3a2 2 0 1 1 0 4v3H2Z" fill="currentColor"/></symbol>
    <symbol id="gear" viewBox="0 0 16 16"><circle cx="6" cy="10" r="4.5" fill="none" stroke="currentColor" stroke-width="2.4"/><circle cx="12" cy="4" r="2.6" fill="none" stroke="currentColor" stroke-width="1.8"/></symbol>
    <symbol id="target" viewBox="0 0 16 16"><circle cx="8" cy="8" r="7" fill="none" stroke="currentColor" stroke-width="1.4"/><circle cx="8" cy="8" r="4" fill="none" stroke="currentColor" stroke-width="1.4"/><circle cx="8" cy="8" r="1.4" fill="currentColor"/></symbol>
    <symbol id="wrench" viewBox="0 0 16 16"><path d="M14 4a4 4 0 0 1-5.2 3.8L3 13.6 2.4 13 8.2 7.2A4 4 0 0 1 12 2l-2 2 2 2Z" fill="currentColor" stroke="currentColor" stroke-width="1.2" stroke-linejoin="round"/></symbol>
    <symbol id="clock" viewBox="0 0 16 16"><circle cx="8" cy="8" r="6.5" fill="none" stroke="currentColor" stroke-width="1.4"/><path d="M8 4.5V8l2.4 1.6" fill="none" stroke="currentColor" stroke-width="1.4" stroke-linecap="round"/></symbol>
    <symbol id="cross" viewBox="0 0 16 16"><path d="M5 5l6 6M11 5l-6 6" stroke="#ff4d5e" stroke-width="1.6" stroke-linecap="round"/></symbol>
  </defs>
</svg>

<!-- Splash -->
<section class="screen screen--blue splash c1 r1">
  <div class="mark"></div>
  <div class="wordmark">PoiseLantern</div>
  <p>Your guide to the most common interview questions, and the best responses to help you get hired</p>
  <div class="start">GET STARTED</div>
</section>

<!-- Welcome -->
<section class="screen screen--blue c2 r1">
  <svg class="welcome-wave" viewBox="0 0 322 702"><path d="M0 0h322v220c-60 30-110 20-170 60-50 30-110 40-152 20Z" fill="#f1f2f7"/></svg>
  <div class="welcome-head"><div class="hello">Welcome to</div><div class="name">PoiseLantern</div></div>
  <div class="welcome-art" role="img" aria-label="Illustration of a candidate and an interviewer talking across a table"></div>
  <nav class="menu">
    <div class="menu-card"><span class="dot-icon dot-icon--teal"><span class="q">?</span></span>View Questions&amp; Responses</div>
    <div class="menu-card"><span class="dot-icon dot-icon--red"><svg style="color:#fff"><use href="#heart"/></svg></span>My Questions Portfolio</div>
    <div class="menu-card"><span class="dot-icon dot-icon--yellow"><svg><use href="#bulb"/></svg></span>Interview Tips</div>
  </nav>
</section>

<!-- Question categories -->
<section class="screen c3 r1">
  <header class="app-bar"><svg class="back"><use href="#chev"/></svg><span class="wordmark">PoiseLantern</span></header>
  <div class="section-bar"><span class="dot-icon dot-icon--teal"><span class="q">?</span></span><h2>View Questions&amp; Responses</h2></div>
  <p class="prompt">Select your question category</p>
  <div class="choice-list">
    <div class="choice"><svg><use href="#puzzle"/></svg>Behavioural</div>
    <div class="choice"><svg><use href="#gear"/></svg>Situational</div>
    <div class="choice"><svg><use href="#target"/></svg>Motivational</div>
    <div class="choice"><svg><use href="#wrench"/></svg>Technical</div>
  </div>
  <div class="pill-btn">See all</div>
</section>

<!-- Behavioural list -->
<section class="screen c1 r2">
  <header class="app-bar"><svg class="back"><use href="#chev"/></svg><span class="wordmark">PoiseLantern</span></header>
  <div class="section-bar"><span class="dot-icon dot-icon--teal"><span class="q">?</span></span><h2>View Questions&amp; Responses</h2></div>
  <div class="band band--teal"><svg><use href="#puzzle"/></svg>Behavioural</div>
  <div class="stack">
    <div class="item"><span class="num num--teal">1</span><p>Lorem ipsum dolor sit amet, consectetuer adipiscing elit, sed diam nonummy nibh euismod tincidunt ut laoreet dolore magna aliquam erat volutpat.</p></div>
    <div class="item"><span class="num num--teal">2</span><p>Lorem ipsum dolor sit amet, consectetuer adipiscing elit, sed diam nonummy nibh euismod tincidunt ut laoreet dolore magna aliquam erat volutpat.</p></div>
    <div class="item"><span class="num num--teal">3</span><p>Lorem ipsum dolor sit amet, consectetuer adipiscing elit, sed diam nonummy nibh euismod</p></div>
    <div class="item" style="min-height:80px"><span class="num num--teal">4</span><p>Lorem ipsum dolor sit amet, consectetuer adipiscing elit</p></div>
    <div class="item"><span class="num num--teal">5</span><p>Lorem ipsum dolor sit amet, consectetuer adipiscing elit, sed diam nonummy nibh euismod tincidunt</p></div>
  </div>
</section>

<!-- Responses -->
<section class="screen c2 r2">
  <header class="app-bar"><svg class="back"><use href="#chev"/></svg><span class="wordmark">PoiseLantern</span></header>
  <div class="section-bar"><span class="dot-icon dot-icon--teal"><span class="q">?</span></span><h2>View Questions&amp; Responses</h2></div>
  <div class="band band--teal"><svg><use href="#puzzle"/></svg>Behavioural</div>
  <div class="carousel carousel--teal" style="padding-top:0">
    <span class="peek peek--l" style="top:0"></span><span class="peek peek--r" style="top:0"></span>
    <div class="item"><span class="num num--teal" style="background:var(--teal)">1</span><p>Lorem ipsum dolor sit amet, consectetuer adipiscing elit, sed diam nonummy nibh euismod tincidunt ut laoreet dolore magna aliquam erat volutpat.</p></div>
    <div class="dots"><i></i><i></i><i></i><i></i><i></i><i></i><i></i><i></i></div>
  </div>
  <div class="responses">
    <div class="response"><span class="tag">Respond 1</span><svg class="fav" style="color:var(--red)"><use href="#heart"/></svg><p>Lorem ipsum dolor sit amet, consectetuer adipiscing elit, sed diam nonummy nibh euismod tincidunt ut laoreet dolore magna ali-</p></div>
    <div class="response"><span class="tag">Respond 2</span><svg class="fav" style="color:#eceef3"><use href="#heart"/></svg><p>Lorem ipsum dolor sit amet, consectetuer adipiscing elit, sed diam nonummy nibh euismod tincidunt ut laoreet dolore magna ali-</p></div>
    <div class="response"><span class="tag">Respond 3</span><svg class="fav" style="color:var(--red)"><use href="#heart"/></svg><p>Lorem ipsum dolor sit amet, consectetuer adipiscing elit, sed diam nonummy nibh euismod tincidunt ut laoreet dolore magna ali-</p></div>
    <div class="response"><span class="tag">Respond 4</span><svg class="fav" style="color:#eceef3"><use href="#heart"/></svg><p>Lorem ipsum dolor sit amet, consectetuer adipiscing elit, sed diam nonummy nibh euismod tincidunt ut laoreet dolore magna ali-</p></div>
  </div>
</section>

<!-- Portfolio -->
<section class="screen c3 r2">
  <header class="app-bar"><svg class="back"><use href="#chev"/></svg><span class="wordmark">PoiseLantern</span></header>
  <div class="section-bar"><span class="dot-icon dot-icon--red"><svg style="color:#fff"><use href="#heart"/></svg></span><h2>My Question Portfolio</h2></div>
  <p class="intro">These are yor saved answers that you favourited. We place them here to help you prepare.</p>
  <div class="saved">
    <div class="saved-card"><span class="num num--red">4</span><svg class="remove"><use href="#cross"/></svg><h3>What are your greatest strengths?</h3><p>Lorem ipsum dolor sit amet, consectetuer adipiscing elit, sed diam nonummy nibh euismod tincidunt ut laoreet dolore magna aliquam erat</p></div>
    <div class="saved-card"><span class="num num--red">20</span><svg class="remove"><use href="#cross"/></svg><h3>Lorem ipsum dolor sit amet?</h3><p>Lorem ipsum dolor sit amet, consectetuer adipiscing elit, sed diam nonummy nibh euismod tincidunt ut laoreet dolore magna aliquam erat</p></div>
    <div class="saved-card"><span class="num num--red">36</span><svg class="remove"><use href="#cross"/></svg><h3>Lorem ipsum dolor sit amet, consectetuer adipiscing elit?</h3><p>Lorem ipsum dolor sit amet, consectetuer adipiscing elit, sed diam nonummy nibh euismod tincidunt ut</p></div>
  </div>
</section>

<!-- Tip categories -->
<section class="screen c1 r3">
  <header class="app-bar"><svg class="back"><use href="#chev"/></svg><span class="wordmark">PoiseLantern</span></header>
  <div class="section-bar section-bar--center"><span class="dot-icon dot-icon--yellow"><svg><use href="#bulb"/></svg></span><h2>Interview Tips</h2></div>
  <p class="prompt">Select your Interview tip category</p>
  <div class="choice-list" style="margin-top:44px">
    <div class="choice choice--left"><svg><use href="#clock"/></svg>Tips for before the interview</div>
    <div class="choice choice--left"><svg><use href="#clock"/></svg>Tips for during the interview</div>
    <div class="choice choice--left"><svg><use href="#clock"/></svg>Tips for after the interview</div>
  </div>
  <div class="pill-btn" style="margin-top:36px">See all</div>
</section>

<!-- Tip list -->
<section class="screen c2 r3">
  <header class="app-bar"><svg class="back"><use href="#chev"/></svg><span class="wordmark">PoiseLantern</span></header>
  <div class="section-bar section-bar--center"><span class="dot-icon dot-icon--yellow"><svg><use href="#bulb"/></svg></span><h2>Interview Tips</h2></div>
  <div class="stack" style="gap:18px;padding-top:18px">
    <div class="item" style="height:56px"><span class="num num--yellow">1</span><p>Start by researching the company an your interviewers</p></div>
    <div class="item" style="height:56px"><span class="num num--yellow">2</span><p>Practice your answers to common interview questions</p></div>
    <div class="item" style="height:56px"><span class="num num--yellow">3</span><p>Re-read the job description</p></div>
    <div class="item" style="height:56px"><span class="num num--yellow">4</span><p>Use th STAR method in answering questions</p></div>
    <div class="item" style="height:56px"><span class="num num--yellow">5</span><p>Recruit a friend to practice answering questions</p></div>
    <div class="item" style="height:56px"><span class="num num--yellow">6</span><p>Prepare a list of references</p></div>
    <div class="item" style="height:56px"><span class="num num--yellow">7</span><p>Be prepered with examples of your work</p></div>
  </div>
</section>

<!-- Tip detail -->
<section class="screen c3 r3">
  <header class="app-bar"><svg class="back"><use href="#chev"/></svg><span class="wordmark">PoiseLantern</span></header>
  <div class="section-bar section-bar--center"><span class="dot-icon dot-icon--yellow"><svg><use href="#bulb"/></svg></span><h2>Interview Tips</h2></div>
  <div class="carousel carousel--yellow" style="padding:20px 0 20px">
    <span class="peek peek--l" style="top:20px;height:56px"></span><span class="peek peek--r" style="top:20px;height:56px"></span>
    <div class="item" style="height:56px"><span class="num num--yellow" style="box-shadow:none">1</span><p>Start by researching the company an your interviewers</p></div>
    <div class="dots"><i></i><i></i><i></i><i></i><i></i><i></i><i></i><i></i></div>
  </div>
  <div class="tip-body">Lorem ipsum dolor sit amet, consectetuer adipiscing elit, sed diam nonummy nibh euismod tincidunt ut laoreet dolore magna aliquam erat volutpat.<br>Ut wisi enim ad minim veniam, quis nostrud exerci tation ullamcorper suscipit lobortis nisl ut aliquip ex ea commodo consequat. Duis autem vel eum iriure dolor in hendrerit in vulputate velit esse molestie</div>
  <div class="ad-slot" role="img" aria-label="Banner advertisement for the mobile game Harbor Siege with a play button"></div>
</section>

</body>
</html>
```